Media Browser and player web application

I need to redesign a web application that enables to browse a media server (Tellavo) contents (images, audio, video) and play it in a web player.

Current implementation of the application can be seen at: http://www.tellavohub.example/content/demonstration-tellavo-pro-online-media-browser

This refresh is aiming to:
1) make the application simpler, based on typology (think Windows Metro style, VidSpire, Flickora); a simple fan concept is here: http://dex.lomarquin.example/tellavo/
2) make the application work on desktop as well as touch screen devices (ie no hover functionality, no pagination, large touch controls)
3) fast (remove unnecessary animations)
4) design with the app being responsive in mind

The attached UX designs show the basic flows in the application. Please note that the placement of controls (for example) is not set in stone and I welcome your input on the layout.

Ideally the default theme will be dark. Items' thumbnails will be square place holders, with images fit in them depending on the item icons' aspect ratio.

Also attaching the product's logo (Tellavo) and icon. The web application's name is ClipRover (or Tellavo ClipRover), so it should be included in the design (the UX designs include place holder Tellavo logo in the left top corner).

The main categories for each file type are (you will have to provide an icon for each of these):
- Audio: Albums, Artists, Album artists, Folders, Genres, Composers, Titles, Random music, Random albums, Last listened, Playlists, Online
- Image: Albums, Folders, Year, Month, Playlists, Online
- Video: Titles, Movies, Series, Folders, Last viewed, Last added, Genres, Actors, Directors, Producers, Release years, Playlists, Online
Updates

Target Market(s)

Mostly tech enthusiasts who want to stream their media over the internet to their devices.

Industry/Entity Type

Artists

Requirements
Must have
• Designs for all the provided UX designs
Touch-friendly web application design
High-res (Retina) assets
Light, type based Metro-like design
Nice to have
• Responsive web version
Dark and Light theme switching.
Should not have
• Chrome
Heavy graphics (eg backgrounds) that take time to load

```html
<!DOCTYPE html>
<html lang="en">
<head>
<meta charset="utf-8">
<title>ClipRover – My Favorites Music</title>
<link rel="stylesheet" href="https://fonts.googleapis.com/css2?family=Open+Sans:wght@400;600&display=swap">
<style>
:root{
  --bg:#121821;
  --row-alt:#19202b;
  --accent:#f7c600;
  --text:#ffffff;
  --muted:#8c939c;
  --rule:#2a313b;
  --rule-strong:#4a515b;
  --btn:#2e343d;
}
*{box-sizing:border-box;margin:0;padding:0}
html,body{width:1200px;height:1078px;overflow:hidden;background:var(--bg);color:var(--text);font-family:"Open Sans",sans-serif}
.app{position:relative;width:1200px;height:1078px}
.brand{position:absolute;left:52px;top:45px;display:flex;align-items:center;gap:10px}
.brand-mark{width:40px;height:40px;background:var(--accent)}
.brand-name{font-size:31px;font-weight:400;color:var(--text);letter-spacing:-0.2px}
.toolbar{position:absolute;top:42px;right:60px;display:flex;gap:8px}
.tool{display:flex;flex-direction:column;align-items:center;width:58px;font-size:14px;color:var(--text);white-space:nowrap}
.tool svg{width:45px;height:45px;margin-bottom:7px}
.topline{position:absolute;left:52px;right:52px;top:131px;border-top:1px solid var(--rule)}
.crumbs{position:absolute;left:51px;top:141px;display:flex;align-items:center;font-size:23px;color:var(--muted)}
.crumbs svg.back{width:46px;height:46px;margin-right:18px}
.crumbs .sep{width:10px;height:12px;margin:0 16px}
.page-title{position:absolute;left:48px;top:198px;font-size:49px;font-weight:400;line-height:1.2}
.list{position:absolute;left:52px;top:287px;width:1096px}
.row{display:grid;grid-template-columns:9px 47px 37px 375px 94px 188px 299px 33px 14px;align-items:center;height:46.9px;font-size:14px}
.row:nth-child(odd){background:var(--row-alt)}
.list-head{display:grid;grid-template-columns:93px 375px 94px 188px 1fr;height:39px;align-items:start;font-size:18px;border-bottom:2px solid var(--rule-strong)}
.list-head span:first-child{grid-column:2}
.thumb{grid-column:2;width:47px;height:47px}
.caret{justify-self:start;margin-left:14px;width:7px;height:8px}
.row.folder .title{color:var(--muted)}
.title{grid-column:4}
.add{grid-column:8;width:33px;height:33px;background:var(--btn);display:flex;align-items:center;justify-content:center}
.add svg{width:14px;height:14px}
</style>
</head>
<body>
<div class="app">
  <div class="brand"><div class="brand-mark"></div><span class="brand-name">ClipRover</span></div>

  <nav class="toolbar">
    <div class="tool"><svg viewBox="0 0 48 48"><circle cx="24" cy="24" r="21.5" fill="none" stroke="var(--accent)" stroke-width="3"/><rect x="13" y="13" width="10" height="10" rx="1.5" fill="var(--accent)"/><rect x="25" y="13" width="10" height="10" rx="1.5" fill="var(--accent)"/><rect x="13" y="25" width="10" height="10" rx="1.5" fill="var(--accent)"/><rect x="25" y="25" width="10" height="10" rx="1.5" fill="var(--accent)"/></svg>Grid View</div>
    <div class="tool"><svg viewBox="0 0 48 48"><circle cx="24" cy="24" r="21.5" fill="none" stroke="var(--accent)" stroke-width="3"/><rect x="18" y="14" width="18" height="3.5" rx="1.5" fill="var(--accent)"/><rect x="18" y="22" width="18" height="3.5" rx="1.5" fill="var(--accent)"/><rect x="18" y="30" width="18" height="3.5" rx="1.5" fill="var(--accent)"/><rect x="12" y="14" width="3" height="3.5" fill="var(--accent)"/><rect x="12" y="22" width="3" height="3.5" fill="var(--accent)"/><rect x="12" y="30" width="3" height="3.5" fill="var(--accent)"/></svg>Queue</div>
    <div class="tool" style="width:72px"><svg viewBox="0 0 48 48"><circle cx="24" cy="24" r="21.5" fill="none" stroke="var(--accent)" stroke-width="3"/><rect x="21" y="12" width="6" height="24" rx="2" fill="var(--accent)"/><rect x="12" y="21" width="24" height="6" rx="2" fill="var(--accent)"/></svg>Enqueue All</div>
    <div class="tool"><svg viewBox="0 0 48 48"><circle cx="24" cy="24" r="21.5" fill="none" stroke="var(--accent)" stroke-width="3"/><circle cx="22" cy="21" r="7.5" fill="none" stroke="var(--accent)" stroke-width="3"/><line x1="27.5" y1="26.5" x2="34" y2="33" stroke="var(--accent)" stroke-width="4" stroke-linecap="round"/></svg>Search</div>
  </nav>

  <div class="topline"></div>

  <div class="crumbs">
    <svg class="back" viewBox="0 0 48 48"><circle cx="24" cy="24" r="22" fill="none" stroke="var(--muted)" stroke-width="3"/><path d="M34 24H15M22 16l-8 8 8 8" fill="none" stroke="var(--muted)" stroke-width="3.5" stroke-linecap="round" stroke-linejoin="round"/></svg>
    <span>Home</span>
    <svg class="sep" viewBox="0 0 10 12"><path d="M0 0l10 6-10 6z" fill="var(--muted)"/></svg>
    <span>Music</span>
    <svg class="sep" viewBox="0 0 10 12"><path d="M0 0l10 6-10 6z" fill="var(--muted)"/></svg>
    <span>Folders</span>
  </div>

  <h1 class="page-title">My Favorites Music</h1>

  <div class="list">
    <div class="list-head"><span>Title</span><span>Duration</span><span>Album</span><span>Artist</span></div>
    <div class="rows">
      <div class="row folder">
        <svg class="thumb" viewBox="0 0 47 47" role="img" aria-label="Folder artwork"><rect width="47" height="47" fill="#2f4a52"/><path d="M13 15h8l2 3h11v13H13z" fill="none" stroke="#fff" stroke-width="2"/></svg>
        <svg class="caret" viewBox="0 0 7 8"><path d="M0 0l7 4-7 4z" fill="var(--muted)"/></svg>
        <span class="title">Old Songs</span>
      </div>
      <div class="row folder">
        <svg class="thumb" viewBox="0 0 47 47"><rect width="47" height="47" fill="#8a8e94"/><path d="M13 15h8l2 3h11v13H13z" fill="none" stroke="#fff" stroke-width="2"/></svg>
        <svg class="caret" viewBox="0 0 7 8"><path d="M0 0l7 4-7 4z" fill="var(--muted)"/></svg>
        <span class="title">From Friends</span>
      </div>
      <div class="row"><div class="thumb" role="img" aria-label="Album cover" style="background:linear-gradient(135deg,#1c2b4a,#7a3a3a)"></div><span class="title">If Then</span><span>3:05</span><span>Back When It Was</span><span>Harbor Lumen</span><span class="add"><svg viewBox="0 0 14 14"><path d="M5 0h4v5h5v4H9v5H5V9H0V5h5z" fill="#fff"/></svg></span></div>
      <div class="row"><div class="thumb" role="img" aria-label="Album cover" style="background:linear-gradient(180deg,#f4c98a,#d9884a)"></div><span class="title">Afterglow</span><span>3:32</span><span>Quiet Remains</span><span>Paper Comets</span><span class="add"><svg viewBox="0 0 14 14"><path d="M5 0h4v5h5v4H9v5H5V9H0V5h5z" fill="#fff"/></svg></span></div>
      <div class="row"><div class="thumb" role="img" aria-label="Album cover" style="background:linear-gradient(135deg,#3a2a1a,#9a3a2a)"></div><span class="title">Who Is Gone ?</span><span>4:15</span><span>Who Is Gone</span><span>Iron Vesper</span><span class="add"><svg viewBox="0 0 14 14"><path d="M5 0h4v5h5v4H9v5H5V9H0V5h5z" fill="#fff"/></svg></span></div>
      <div class="row"><div class="thumb" role="img" aria-label="Album cover" style="background:linear-gradient(135deg,#8aa0b0,#1f2a3a)"></div><span class="title">Stay Close, We're Heading Home</span><span>3:14</span><span>Unknown</span><span>Dell Marrow</span><span class="add"><svg viewBox="0 0 14 14"><path d="M5 0h4v5h5v4H9v5H5V9H0V5h5z" fill="#fff"/></svg></span></div>
      <div class="row"><div class="thumb" role="img" aria-label="Album cover" style="background:linear-gradient(180deg,#b8b8b8,#2a2a2a)"></div><span class="title">If Then</span><span>3:05</span><span>Back When It Was</span><span>Harbor Lumen</span><span class="add"><svg viewBox="0 0 14 14"><path d="M5 0h4v5h5v4H9v5H5V9H0V5h5z" fill="#fff"/></svg></span></div>
      <div class="row"><div class="thumb" role="img" aria-label="Album cover" style="background:#050608"></div><span class="title">Afterglow</span><span>3:32</span><span>Quiet Remains</span><span>Paper Comets</span><span class="add"><svg viewBox="0 0 14 14"><path d="M5 0h4v5h5v4H9v5H5V9H0V5h5z" fill="#fff"/></svg></span></div>
      <div class="row"><div class="thumb" role="img" aria-label="Album cover" style="background:linear-gradient(135deg,#cfe6ee,#2a3a48)"></div><span class="title">Who Is Gone ?</span><span>4:15</span><span>Who Is Gone</span><span>Iron Vesper</span><span class="add"><svg viewBox="0 0 14 14"><path d="M5 0h4v5h5v4H9v5H5V9H0V5h5z" fill="#fff"/></svg></span></div>
      <div class="row"><div class="thumb" role="img" aria-label="Album cover" style="background:linear-gradient(135deg,#5a4a3a,#1e1a16)"></div><span class="title">Stay Close, We're Heading Home</span><span>3:14</span><span>Unknown</span><span>Dell Marrow</span><span class="add"><svg viewBox="0 0 14 14"><path d="M5 0h4v5h5v4H9v5H5V9H0V5h5z" fill="#fff"/></svg></span></div>
      <div class="row"><div class="thumb" role="img" aria-label="Album cover" style="background:linear-gradient(180deg,#e8dcd0,#b07a90)"></div><span class="title">If Then</span><span>3:05</span><span>Back When It Was</span><span>Harbor Lumen</span><span class="add"><svg viewBox="0 0 14 14"><path d="M5 0h4v5h5v4H9v5H5V9H0V5h5z" fill="#fff"/></svg></span></div>
      <div class="row"><div class="thumb" role="img" aria-label="Album cover" style="background:linear-gradient(180deg,#d8202a,#1a0a0a)"></div><span class="title">Afterglow</span><span>3:32</span><span>Quiet Remains</span><span>Paper Comets</span><span class="add"><svg viewBox="0 0 14 14"><path d="M5 0h4v5h5v4H9v5H5V9H0V5h5z" fill="#fff"/></svg></span></div>
    </div>
  </div>
</div>
</body>
</html>
```